Poster design for "A Frame" Sign

I need a design for an A Frame sign. Measurements and Specifications here:
http://www.brodexsupply.com.au/pg/a-boards/ABPBBLKPRT-Print-Specs.pdf

Actually, it will need to be two designs, one with an arrow pointing left and one with an arrow pointing right, otherwise exactly the same.

LOGO to be used is attached. Colours of design should match logo and should also include orange tones.

The A Frame sign is to be put on the driveway of my home studio at a main road in a residential suburban area. Cars drive by at around 50 km/h, so there needs to be an eye catcher that there is a nurturing home massage studio here.

Logo can be left or right, somehow incorporated into the text below:
-
[Big header, ideally "LeHavre" font]
Tarova Calm
Massage Studio

[slightly smaller font, serif, with bullet points]
- Relaxation Massage
- Remedial Massage
- Pregnancy Massage
- Kahuna Massage

[big Arrow to the left/right - one for each side of the frame]

[sans serif font, same size as above]
Bookings essential!
ph 0491 857 604
www.tarovacalm.com.au

[serif font, same as above]
EFTPOS and instant health fund claims available.
-

Residential

f37022

```html
<!DOCTYPE html>
<html lang="en">
<head>
<meta charset="utf-8">
<title>Tarova Calm Massage Studio – A-Frame Signs</title>
<link href="https://fonts.googleapis.com/css2?family=Sniglet:wght@400;800&family=Urbanist:ital,wght@0,500;0,600;1,600&display=swap" rel="stylesheet">
<style>
  :root {
    --canvas: #ffffff;
    --edge-top: #ee86be;
    --edge-bottom: #c99de9;
    --panel-top: #e77cba;
    --panel-mid: #dc8ccd;
    --panel-bottom: #c7a0ec;
    --frame: #ffffff;
    --band: #c8416b;
    --band-dark: #b63660;
    --arrow: #ffffff;
    --ink: #111111;
    --brand: #d9387a;
  }
  * { margin: 0; padding: 0; box-sizing: border-box; }
  html, body { width: 1200px; height: 800px; overflow: hidden; background: var(--canvas); }
  .canvas { position: relative; width: 1200px; height: 800px; }

  .sign {
    position: absolute; top: 42px; width: 484px; height: 715px; overflow: hidden;
    background: linear-gradient(180deg, var(--edge-top), var(--edge-bottom));
  }
  .sign--right { left: 27px; }
  .sign--left { left: 688px; }

  .sign__panel {
    position: absolute; left: 11px; top: 13px; right: 13px; bottom: 14px;
    border: 5px solid var(--frame);
    background: linear-gradient(180deg, var(--panel-top) 0%, var(--panel-mid) 55%, var(--panel-bottom) 100%);
    box-shadow: 0 0 4px rgba(0,0,0,0.25);
  }

  .brand-mark {
    position: absolute; top: 65px; left: 0; width: 484px; height: 80px;
    display: flex; align-items: center; justify-content: center; gap: 12px;
  }
  .brand-mark__dot {
    width: 80px; height: 80px; border-radius: 50%; background: var(--brand);
  }
  .brand-mark__name {
    font-family: 'Sniglet', cursive; font-weight: 800; font-size: 30px; color: var(--brand);
  }

  .title {
    position: absolute; top: 158px; left: 0; width: 484px; text-align: center;
    font-family: 'Sniglet', cursive; font-weight: 800; font-variant: small-caps;
    font-size: 54px; line-height: 64px; color: var(--ink); letter-spacing: 0.5px;
  }

  .services {
    position: absolute; top: 291px; left: 60px; list-style: none;
    font-family: 'Urbanist', sans-serif; font-weight: 600; font-size: 30px; line-height: 40.5px;
    letter-spacing: 2px; color: var(--ink); white-space: nowrap;
  }
  .services li::before { content: "\2022"; margin-right: 6px; }

  .direction-band {
    position: absolute; left: 0; top: 461px; width: 484px; height: 90px;
    background: linear-gradient(180deg, var(--band), var(--band-dark));
  }
  .direction-band svg { display: block; }

  .contact {
    position: absolute; top: 566px; left: 0; width: 484px; text-align: center;
    font-family: 'Urbanist', sans-serif; font-weight: 600; color: var(--ink); letter-spacing: 2px;
    white-space: nowrap;
  }
  .contact__note { font-size: 23px; font-style: italic; line-height: 32px; }
  .contact__line { font-size: 24px; line-height: 31px; }
  .contact__small { font-size: 15px; font-weight: 500; letter-spacing: 0; margin-top: 4px; line-height: 20px; }
</style>
</head>
<body>
<main class="canvas">

  <section class="sign sign--right" aria-label="A-frame sign with arrow pointing right">
    <div class="sign__panel"></div>
    <div class="brand-mark"><span class="brand-mark__dot"></span><span class="brand-mark__name">Tarova Calm</span></div>
    <h1 class="title">Tarova Calm<br>Massage Studio</h1>
    <ul class="services">
      <li>Relaxation Massage</li>
      <li>Remedial Massage</li>
      <li>Pregnancy Massage</li>
      <li>Kahuna Massage</li>
    </ul>
    <div class="direction-band">
      <svg width="484" height="90" viewBox="0 0 484 90" aria-hidden="true">
        <polygon fill="var(--arrow)" points="43,24 353,24 353,5 441,45 353,85 353,66 43,66"/>
      </svg>
    </div>
    <div class="contact">
      <p class="contact__note">BOOKINGS ESSENTIAL!</p>
      <p class="contact__line">ph 0491 857 604</p>
      <p class="contact__line">www.tarovacalm.com.au</p>
      <p class="contact__small">EFTPOS and Instant Health Fund Claims Available.</p>
    </div>
  </section>

  <section class="sign sign--left" aria-label="A-frame sign with arrow pointing left">
    <div class="sign__panel"></div>
    <div class="brand-mark"><span class="brand-mark__dot"></span><span class="brand-mark__name">Tarova Calm</span></div>
    <h1 class="title">Tarova Calm<br>Massage Studio</h1>
    <ul class="services">
      <li>Relaxation Massage</li>
      <li>Remedial Massage</li>
      <li>Pregnancy Massage</li>
      <li>Kahuna Massage</li>
    </ul>
    <div class="direction-band">
      <svg width="484" height="90" viewBox="0 0 484 90" aria-hidden="true">
        <polygon fill="var(--arrow)" points="441,24 131,24 131,5 43,45 131,85 131,66 441,66"/>
      </svg>
    </div>
    <div class="contact">
      <p class="contact__note">BOOKINGS ESSENTIAL!</p>
      <p class="contact__line">ph 0491 857 604</p>
      <p class="contact__line">www.tarovacalm.com.au</p>
      <p class="contact__small">EFTPOS and Instant Health Fund Claims Available.</p>
    </div>
  </section>

</main>
</body>
</html>
```